TARPLOAD business card design

TARPLOAD is a manufacturer of skip bags supplying both the domestic and commercial market. We wish to convey core characteristics of strength, professionalism and reliability to our customers. We are after a business card that uses our company colours of black and yellow as well as incorporating our logo. Our customers are predominantly in the construction or hardware industry. It is important the cards are professional as we are a small company wishing to appear larger than we actually are. more info on the company and product available at www.tarpload-example.com.au

Target Market(s)

hardware buyers, contruction company owners

Industry/Entity Type

Construction

Requirements
Must have
• company colours of black and yellow - No other colours or variation of yellow black. our company logo. card design must convey "tough"
• Card design must be landscape
• Details to be included on the card are:
• Name and Tiltle
• Phone number : 1300 41 62 53
• Mobile: 0452 718 903
• Fax: 03 9617 4852
• email: dale.hendry@tarpload-example.com.au
• address: PO Box 517, Kelvindale, VIC,3294
• Text in white when on a black background
Nice to have
• I like the idea of the back of the card being black with lighter circle area in the middle with black logo in the centre. Similar to the attached "iconic" card

```html
<!DOCTYPE html>
<html lang="en">
<head>
<meta charset="utf-8">
<title>TARPLOAD business cards</title>
<link href="https://fonts.googleapis.com/css2?family=Krona+One&family=Arimo:wght@400;700&display=swap" rel="stylesheet">
<style>
  :root {
    --black: #000000;
    --yellow: #ebcd00;
    --white: #ffffff;
    --page: #ffffff;
  }
  * { margin: 0; padding: 0; box-sizing: border-box; }
  html, body {
    width: 1200px; height: 2182px; overflow: hidden;
    background: var(--page);
    font-family: "Arimo", Arial, sans-serif;
  }
  .card { position: absolute; overflow: hidden; }
  .card--front-dark { left: 0; top: 0; width: 1191px; height: 693px; background: var(--black); color: var(--white); }
  .card--back { left: 7px; top: 745px; width: 1189px; height: 695px; background: var(--black); }
  .card--front-light { left: 11px; top: 1487px; width: 1189px; height: 691px; background: var(--yellow); color: var(--black); border: 2px solid var(--black); }

  .brand {
    position: absolute;
    font-family: "Arimo", Arial, sans-serif;
    font-weight: 700;
    line-height: 1;
    letter-spacing: 1px;
  }
  .card--front-dark .brand { left: 80px; top: 360px; font-size: 50px; color: var(--yellow); }
  .card--front-light .brand { left: 78px; top: 345px; font-size: 50px; color: var(--black); }
  .card--back .brand { left: 69px; top: 392px; font-size: 108px; color: var(--yellow); }

  .divider { position: absolute; left: 385px; top: 180px; width: 4px; height: 344px; }
  .card--front-dark .divider { background: var(--yellow); }
  .card--front-light .divider { background: var(--black); left: 381px; top: 182px; height: 344px; }

  .details { position: absolute; left: 449px; top: 172px; }
  .card--front-light .details { left: 446px; top: 172px; }
  .name {
    font-family: "Krona One", Arial, sans-serif;
    font-size: 42px; line-height: 1; letter-spacing: 1px;
  }
  .title {
    margin-top: 16px;
    font-weight: 700; font-size: 24px; letter-spacing: 2px;
  }
  .contact { margin-top: 70px; font-size: 27px; line-height: 32px; }
  .phones { margin-top: 46px; font-size: 27px; line-height: 34px; }
  .label { font-size: 18px; text-transform: uppercase; margin-right: 8px; }
  .contact .label { font-size: 27px; text-transform: none; margin-right: 10px; }
</style>
</head>
<body>

<section class="card card--front-dark">
  <div class="brand">TARPLOAD</div>
  <div class="divider"></div>
  <div class="details">
    <div class="name">DALE HENDRY</div>
    <div class="title">MANAGING DIRECTOR</div>
    <div class="contact">
      <div><span class="label">e:</span>dale.hendry@tarpload-example.com.au</div>
      <div><span class="label">a:</span>PO Box 517, Kelvindale, VIC,3294</div>
    </div>
    <div class="phones">
      <div><span class="label">p:</span>1 300 41 62 53 | <span class="label">m:</span>0452 718 903</div>
      <div><span class="label">f:</span>&nbsp;03&nbsp; 9617 4852</div>
    </div>
  </div>
</section>

<section class="card card--back">
  <div class="brand">TARPLOAD</div>
</section>

<section class="card card--front-light">
  <div class="brand">TARPLOAD</div>
  <div class="divider"></div>
  <div class="details">
    <div class="name">DALE HENDRY</div>
    <div class="title">MANAGING DIRECTOR</div>
    <div class="contact">
      <div><span class="label">e:</span>dale.hendry@tarpload-example.com.au</div>
      <div><span class="label">a:</span>PO Box 517, Kelvindale, VIC,3294</div>
    </div>
    <div class="phones">
      <div><span class="label">p:</span>1 300 41 62 53 | <span class="label">m:</span>0452 718 903</div>
      <div><span class="label">f:</span>&nbsp;03&nbsp; 9617 4852</div>
    </div>
  </div>
</section>

</body>
</html>
```